A start-up named "Corvath Therapeutics" - needs a new PowerPoint design

We need a new PowerPoint Design for an early-stage start-up named "Corvath Therapeutics" seeking to disrupt the current approach towards drug discovery within aging disorders.

We would like to build on Corvath's legacy, the founder of the modern science of genetics, by employing a multidisciplinary approach, experimenting, and providing elderly patients the attention they deserve.

We have selected the suffix "therapeutics" intentionally as it stands for (a medicine) the treatment of disease; the science of healing. Alzheimer’s treatment is a huge, urgent, unmet need:
- Shift from a disease-management system to a preventive medicine system
- Focus on increasing the health span, not only the life span

Target Market(s)

Pharma/ Biotech Executives Medical Institutions Healthcare professionals (MDs, nurses, payors, pharmacists, etc.) Patients

Industry/Entity Type

Healthcare

Other font styles liked:
• Celias

Colors
0054AA
0677BA
7BADD7
CADEEF
E8F1F8
E54698
E96AAD
F1A4CE
F9D9EA
FCEFF6
A7469A
B969AE
D3A5CF
EDDBEB
F8F0F9
6B429C
8869AF
B7A5CE
E3DAEB
F3F0F8

Requirements
Must have
• - differentiate from other companies named after Corvath - differentiate from other Pharma/ Biotech companies
Nice to have
• simplicity/ minimalist logo vivid colors gradient 3D Life-Sciences inspired Simple geometry Balance
Should not have
• mascot/ emblem watermark logo animated ink style nature-inspired inventive typography artistic chaos

```html
<!DOCTYPE html>
<html lang="en">
<head>
<meta charset="utf-8">
<title>Corvath Therapeutics — Presentation Slides</title>
<link href="https://fonts.googleapis.com/css2?family=Montserrat:wght@400;500;600;700;800&display=swap" rel="stylesheet">
<style>
:root{
  --cyan:#12c0f0;
  --blue:#0677ba;
  --deep-blue:#0054aa;
  --violet:#6b429c;
  --purple:#8a2a9c;
  --magenta:#a7469a;
  --pink:#e54698;
  --ink:#222230;
  --grey:#dcdce2;
  --bg-top:#5a1f6e;
  --bg-bottom:#0b0d24;
  --band:linear-gradient(90deg,var(--cyan),#3c86d6 45%,var(--violet) 80%,var(--purple));
}
*{box-sizing:border-box;margin:0;padding:0}
html,body{width:1200px;height:1098px;overflow:hidden}
body{
  font-family:"Montserrat",sans-serif;color:var(--ink);position:relative;
  background:linear-gradient(160deg,var(--bg-top) 0%,#2a1138 40%,#161433 62%,var(--bg-bottom) 100%);
}
.slide{position:absolute;width:487px;height:274px;background:#fff;overflow:hidden;box-shadow:0 6px 18px rgba(0,0,0,.45)}
.slide--cover{background:#050508}
.s1{left:99px;top:107px}.s2{left:614px;top:107px}
.s3{left:99px;top:412px}.s4{left:614px;top:412px}
.s5{left:99px;top:718px}.s6{left:614px;top:718px}
.abs{position:absolute}

/* header */
.header-band{position:absolute;top:23px;left:0;height:12px;background:var(--band)}
.header-cap{position:absolute;top:23px;right:0;height:12px;width:32px;background:var(--purple)}
.brand{position:absolute;top:14px;display:flex;align-items:center;gap:5px;color:var(--blue);font-weight:600}
.brand-mark{width:9px;height:9px;border-radius:50%;background:var(--blue);flex:none}
.brand-name{font-size:13px;line-height:13px}
.brand-name small{display:block;font-size:7.4px;line-height:9px;letter-spacing:.9px}

/* cover */
.cover-brand{position:absolute;left:130px;top:96px;display:flex;align-items:center;gap:12px;color:var(--cyan);font-weight:600}
.cover-brand .brand-mark{width:16px;height:16px;background:var(--cyan)}
.cover-brand .name{font-size:36px;line-height:36px}
.cover-brand .name small{display:block;font-size:16px;line-height:22px;letter-spacing:2.6px}
.cover-band{position:absolute;left:0;right:0;top:210px;height:23px;background:var(--band)}
.cover-glow{position:absolute;inset:0;background:linear-gradient(135deg,transparent 40%,rgba(40,60,80,.25) 55%,transparent 70%)}

/* text */
.tiny{font-size:5.2px;line-height:6.3px;color:#555}
.small{font-size:6.6px;line-height:7.4px;color:#333}
.head-lbl{font-size:5.6px;letter-spacing:.5px;color:#333;font-weight:500}
.title-blue{font-weight:800;color:var(--deep-blue);font-size:17px;letter-spacing:-.2px}
.title-dark{font-weight:800;font-size:17px;letter-spacing:2.8px;color:var(--ink)}
.center{text-align:center}

/* gauges */
.gauge{position:absolute;width:70px;text-align:center}
.divider{position:absolute;width:1px;background:#666}

/* check list */
.checklist{position:absolute;list-style:none}
.checklist li{display:flex;gap:8px;align-items:flex-start;margin-bottom:8px}
.checklist svg{flex:none}

/* legend */
.legend{display:flex;align-items:flex-start;gap:6px}
.swatch{width:8px;height:8px;flex:none;margin-top:1px}

/* market */
.opp{position:absolute;left:208px;width:245px}
.opp-item{display:flex;gap:8px;padding:4px 0 3px;border-bottom:1px solid #3c86d6}
.opp-item:last-child{border-bottom:none}
.opp-item h4{font-size:7.4px;font-weight:700;color:var(--deep-blue);line-height:8px}
.opp-item p{font-size:6.6px;line-height:7.6px;color:#333}

.num{position:absolute;width:32px;height:32px;border-radius:50%}
.num-text{position:absolute}
.num-text b{display:block;font-size:11px;font-weight:600;line-height:12px}
</style>
</head>
<body>

<!-- Slide 1: cover -->
<section class="slide slide--cover s1">
  <div class="cover-glow"></div>
  <div class="cover-brand">
    <span class="brand-mark"></span>
    <div class="name">Corvath<small>Therapeutics</small></div>
  </div>
  <div class="cover-band"></div>
</section>

<!-- Slide 2: key figures -->
<section class="slide s2">
  <div class="header-band" style="width:309px;top:22px"></div>
  <div class="brand" style="left:324px"><span class="brand-mark"></span><div class="brand-name">Corvath<small>Therapeutics</small></div></div>
  <div class="header-cap" style="top:22px;width:51px"></div>

  <svg class="abs" style="left:0;top:0" width="260" height="274" aria-hidden="true">
    <defs>
      <linearGradient id="g-ring" x1="0" y1="0" x2="1" y2="1"><stop offset="0" stop-color="#8a2a9c"/><stop offset="1" stop-color="#3c4fc8"/></linearGradient>
      <linearGradient id="g-ring-b" x1="0" y1="0" x2="1" y2="1"><stop offset="0" stop-color="#12c0f0"/><stop offset="1" stop-color="#1b6fd0"/></linearGradient>
    </defs>
    <g fill="none" stroke-width="3.2" stroke-linecap="butt">
      <circle cx="69" cy="97" r="19" stroke="url(#g-ring)" stroke-dasharray="95 120" transform="rotate(-60 69 97)"/>
      <circle cx="144" cy="97" r="19" stroke="url(#g-ring-b)" stroke-dasharray="60 120" transform="rotate(0 144 97)"/>
      <circle cx="219" cy="97" r="19" stroke="url(#g-ring)" stroke-dasharray="75 120" transform="rotate(-90 219 97)"/>
      <circle cx="69" cy="181" r="19" stroke="url(#g-ring)" stroke-dasharray="70 120" transform="rotate(-230 69 181)"/>
      <circle cx="144" cy="181" r="19" stroke="url(#g-ring-b)" stroke-dasharray="70 120" transform="rotate(-230 144 181)"/>
      <circle cx="219" cy="181" r="19" stroke="url(#g-ring)" stroke-dasharray="45 120" transform="rotate(-190 219 181)"/>
    </g>
    <g font-family="Montserrat,sans-serif" font-size="9" fill="#444" text-anchor="middle" font-weight="500">
      <text x="69" y="100">1.8</text><text x="144" y="100">3.5</text><text x="219" y="100">9.5</text>
      <text x="72" y="184">30%</text><text x="146" y="184">10%</text><text x="222" y="184">34%</text>
    </g>
  </svg>
  <div class="divider" style="left:107px;top:76px;height:145px"></div>
  <div class="divider" style="left:184px;top:76px;height:145px"></div>
  <div class="divider" style="left:309px;top:76px;height:145px"></div>

  <div class="gauge" style="left:34px;top:126px"><div class="head-lbl">HEADLINE</div><div class="tiny">Lorem ipsum dolor sit amet consectetur adipiscing elit, sed do</div></div>
  <div class="gauge" style="left:109px;top:126px"><div class="head-lbl">HEADLINE</div><div class="tiny">Lorem ipsum dolor sit amet consectetur adipiscing elit, sed do</div></div>
  <div class="gauge" style="left:184px;top:126px"><div class="head-lbl">HEADLINE</div><div class="tiny">Lorem ipsum dolor sit amet consectetur adipiscing elit, sed do</div></div>
  <div class="gauge" style="left:32px;top:210px"><div class="head-lbl">HEADLINE</div><div class="tiny">Lorem ipsum dolor sit amet consectetur adipiscing elit, sed do</div></div>
  <div class="gauge" style="left:108px;top:210px"><div class="head-lbl">HEADLINE</div><div class="tiny">Lorem ipsum dolor sit amet consectetur adipiscing elit, sed do</div></div>
  <div class="gauge" style="left:184px;top:210px"><div class="head-lbl">HEADLINE</div><div class="tiny">Lorem ipsum dolor sit amet consectetur adipiscing elit, sed do</div></div>

  <div class="abs" style="left:316px;top:76px;width:150px">
    <div class="title-dark">Title Here</div>
    <p class="small" style="margin-top:8px">Lorem ipsum dolor sit amet, consectetur adipiscing elit. Etiam iaculis commodo.</p>
    <p class="small" style="margin-top:8px">Lorem ipsum dolor sit amet, consectetur adipiscing elit. Etiam iaculis commod.</p>
    <p class="small" style="margin-top:16px">Lorem ipsum dolor sit amet, consectetur adipiscing elit. Etiam iaculis commod.</p>
    <p class="small" style="margin-top:8px">Lorem ipsum dolor sit amet, consectetur adipiscing elit. Etiam iaculis commod.</p>
  </div>
</section>

<!-- Slide 3: share chart -->
<section class="slide s3">
  <div class="header-band" style="width:329px"></div>
  <div class="brand" style="left:339px"><span class="brand-mark"></span><div class="brand-name">Corvath<small>Therapeutics</small></div></div>
  <div class="header-cap"></div>

  <p class="small abs" style="left:37px;top:50px;width:160px">Lorem ipsum dolor sit amet, consectetur adipiscing elit. Etiam iaculis commod.</p>

  <svg class="abs" style="left:30px;top:80px" width="130" height="110" aria-hidden="true">
    <defs>
      <linearGradient id="g-bar" x1="0" y1="0" x2="0" y2="1"><stop offset="0" stop-color="#3c86d6"/><stop offset="1" stop-color="#8a2a9c"/></linearGradient>
      <linearGradient id="g-bar2" x1="0" y1="0" x2="0" y2="1"><stop offset="0" stop-color="#8a2a9c"/><stop offset="1" stop-color="#12c0f0"/></linearGradient>
    </defs>
    <rect x="16" y="81" width="5" height="16" fill="#8a2a9c"/>
    <rect x="24" y="70" width="5" height="27" fill="url(#g-bar)"/>
    <rect x="33" y="37" width="5" height="60" fill="url(#g-bar)"/>
    <rect x="42" y="8" width="5" height="89" fill="url(#g-bar)"/>
    <rect x="75" y="81" width="5" height="16" fill="#12c0f0"/>
    <rect x="83" y="59" width="5" height="38" fill="#3c86d6"/>
    <rect x="92" y="37" width="5" height="60" fill="url(#g-bar2)"/>
    <rect x="101" y="8" width="5" height="89" fill="url(#g-bar2)"/>
  </svg>
  <div class="small abs" style="left:37px;top:189px">Lorem ipsum</div>
  <div class="small abs" style="left:96px;top:189px">Lorem ipsum</div>

  <svg class="abs" style="left:180px;top:72px" width="130" height="130" aria-hidden="true">
    <defs><linearGradient id="g-pie" x1="1" y1="0" x2="0" y2="1"><stop offset="0" stop-color="#12c0f0"/><stop offset=".5" stop-color="#3c86d6"/><stop offset="1" stop-color="#6b429c"/></linearGradient></defs>
    <circle cx="65" cy="65" r="60" fill="url(#g-pie)"/>
    <circle cx="65" cy="65" r="60" fill="none" stroke="#111" stroke-width="1.6" stroke-dasharray="280 400" transform="rotate(0 65 65)"/>
    <text x="61" y="73" text-anchor="middle" font-family="Montserrat,sans-serif" font-size="24" font-weight="800" fill="#fff" font-style="italic">75%</text>
  </svg>

  <div class="legend abs" style="left:350px;top:142px"><span class="swatch" style="background:var(--violet)"></span><span class="small" style="font-size:7.4px;line-height:8px">Lorem ipsum dolor<br>sit amet, co.</span></div>
  <div class="legend abs" style="left:350px;top:175px"><span class="swatch" style="background:var(--violet)"></span><span class="small" style="font-size:7.4px;line-height:8px">Lorem ipsum dolor<br>sit amet, co.</span></div>

  <div class="abs" style="left:37px;top:218px;width:414px;height:1px;background:#555"></div>
  <p class="small abs center" style="left:37px;top:224px;width:414px;font-size:6.2px">Lorem ipsum dolor sit amet, consectetur adipiscing elit. Etiam iaculis commod. Lorem ipsum dolor sit amet, consectetur adipiscing elit. Etiam iaculis commod. Lorem ipsum dolor sit amet, consectetur adipiscing elit. Etiam iaculis commod. Lorem ipsum dolor sit amet, consectetur adipiscing elit. Etiam iaculis commod.</p>
</section>

<!-- Slide 4: overlap diagram -->
<section class="slide s4">
  <div class="header-band" style="width:329px"></div>
  <div class="brand" style="left:339px"><span class="brand-mark"></span><div class="brand-name">Corvath<small>Therapeutics</small></div></div>
  <div class="header-cap"></div>

  <div class="title-blue abs" style="left:35px;top:80px">TITLE HERE</div>
  <ul class="checklist" style="left:35px;top:106px;width:130px">
    <li><svg width="18" height="18" viewBox="0 0 18 18"><rect x="1" y="3" width="14" height="14" fill="none" stroke="#3c4fc8" stroke-width="1.6"/><path d="M4 10l4 4 9-12" fill="none" stroke="#3c4fc8" stroke-width="1.8"/></svg><span class="small" style="font-size:6px;line-height:6.8px">Lorem ipsum dolor sit amet, consectetur adipiscing elit. Etiam iaculis commodo.</span></li>
    <li><svg width="18" height="18" viewBox="0 0 18 18"><rect x="1" y="3" width="14" height="14" fill="none" stroke="#3c4fc8" stroke-width="1.6"/><path d="M4 10l4 4 9-12" fill="none" stroke="#3c4fc8" stroke-width="1.8"/></svg><span class="small" style="font-size:6px;line-height:6.8px">Lorem ipsum dolor sit amet, consectetur adipiscing elit. Etiam iaculis commod.</span></li>
    <li><svg width="18" height="18" viewBox="0 0 18 18"><rect x="1" y="3" width="14" height="14" fill="none" stroke="#3c4fc8" stroke-width="1.6"/><path d="M4 10l4 4 9-12" fill="none" stroke="#3c4fc8" stroke-width="1.8"/></svg><span class="small" style="font-size:6px;line-height:6.8px">Lorem ipsum dolor sit amet, consectetur adipiscing elit. Etiam iaculis commod.</span></li>
    <li><svg width="18" height="18" viewBox="0 0 18 18"><rect x="1" y="3" width="14" height="14" fill="none" stroke="#3c4fc8" stroke-width="1.6"/><path d="M4 10l4 4 9-12" fill="none" stroke="#3c4fc8" stroke-width="1.8"/></svg><span class="small" style="font-size:6px;line-height:6.8px">Lorem ipsum dolor sit amet, consectetur adipiscing elit. Etiam iaculis commod.</span></li>
  </ul>

  <svg class="abs" style="left:180px;top:60px" width="300" height="160" aria-hidden="true">
    <defs>
      <linearGradient id="g-v1" x1="0" y1="0" x2="1" y2="1"><stop offset="0" stop-color="#a7469a"/><stop offset="1" stop-color="#6b2a9c"/></linearGradient>
      <linearGradient id="g-v2" x1="0" y1="0" x2="1" y2="1"><stop offset="0" stop-color="#1b7fd8"/><stop offset="1" stop-color="#12b6ec"/></linearGradient>
      <linearGradient id="g-v3" x1="0" y1="0" x2="1" y2="1"><stop offset="0" stop-color="#12c0f0"/><stop offset="1" stop-color="#1b6fd0"/></linearGradient>
    </defs>
    <circle cx="114" cy="56" r="42" fill="url(#g-v1)" opacity=".95"/>
    <circle cx="181" cy="74" r="42" fill="url(#g-v2)" opacity=".9"/>
    <circle cx="138" cy="102" r="42" fill="url(#g-v3)" opacity=".85"/>
    <g fill="none" stroke="#fff" stroke-width="1.2">
      <rect x="104" y="42" width="14" height="18"/><path d="M108 55l3-4 3 2 2-4"/>
      <rect x="171" y="63" width="20" height="13"/><path d="M177 80h8M181 76v4"/>
      <rect x="131" y="108" width="16" height="14"/><path d="M135 108v-4a4 4 0 0 1 8 0v4"/>
    </g>
    <g fill="none" stroke="#555" stroke-width=".7">
      <path d="M237 30l-11 16"/><path d="M72 77h-22l-7 5"/><path d="M189 146h27"/>
    </g>
    <g font-family="Montserrat,sans-serif" font-weight="700" fill="#8a2a9c" font-size="12">
      <text x="190" y="23">32%</text><text x="66" y="106">21%</text><text x="186" y="140">45%</text>
    </g>
    <g font-family="Montserrat,sans-serif" fill="#555" font-size="5">
      <text x="225" y="17">Lorem ipsum dolor</text><text x="225" y="23">sit amet consectetur</text>
      <text x="8" y="99">Lorem ipsum dolor</text><text x="8" y="105">sit amet consectetur</text>
      <text x="220" y="133">Lorem ipsum dolor</text><text x="220" y="139">sit amet consectetur</text>
    </g>
  </svg>

  <div class="legend abs" style="left:230px;top:228px"><span class="swatch" style="background:var(--magenta);width:12px;height:12px"></span><span class="tiny">Lorem ipsum<br>dolor sit</span></div>
  <div class="legend abs" style="left:301px;top:228px"><span class="swatch" style="background:linear-gradient(135deg,#1b6fd0,#12c0f0);width:12px;height:12px"></span><span class="tiny">Lorem ipsum<br>dolor sit</span></div>
  <div class="legend abs" style="left:372px;top:228px"><span class="swatch" style="background:#12b6ec;width:12px;height:12px"></span><span class="tiny">Lorem ipsum<br>dolor sit</span></div>
</section>

<!-- Slide 5: market opportunities -->
<section class="slide s5">
  <div class="header-band" style="width:329px"></div>
  <div class="brand" style="left:339px"><span class="brand-mark"></span><div class="brand-name">Corvath<small>Therapeutics</small></div></div>
  <div class="header-cap"></div>

  <svg class="abs" style="left:0;top:40px" width="140" height="234" aria-hidden="true">
    <defs><linearGradient id="g-seg" x1="0" y1="0" x2="0" y2="1"><stop offset="0" stop-color="#1b5fb8"/><stop offset="1" stop-color="#0054aa"/></linearGradient></defs>
    <g transform="translate(19 116)">
      <path d="M0 -112 A112 112 0 0 1 60 -95 L27 -43 A50 50 0 0 0 0 -50Z" fill="url(#g-seg)"/>
      <path d="M0 -112 L0 -50 A50 50 0 0 0 -50 0 L-112 0 A112 112 0 0 1 0 -112Z" fill="#0b5ab8"/>
      <path d="M60 -95 A112 112 0 0 1 100 -50 L45 -22 A50 50 0 0 0 27 -43Z" fill="#ec3f8a"/>
      <path d="M100 -50 A112 112 0 0 1 110 20 L49 9 A50 50 0 0 0 45 -22Z" fill="#e0316f"/>
      <path d="M110 20 A112 112 0 0 1 80 78 L36 35 A50 50 0 0 0 49 9Z" fill="#c92c6e"/>
      <path d="M80 78 A112 112 0 0 1 30 108 L13 48 A50 50 0 0 0 36 35Z" fill="#b0307a"/>
      <path d="M30 108 A112 112 0 0 1 -112 0 L-50 0 A50 50 0 0 0 13 48Z" fill="#8a2a9c"/>
      <circle r="10" fill="#3c86d6"/>
      <path d="M0 -10 A10 10 0 0 1 0 10Z" fill="#8a2a9c"/>
      <g fill="none" stroke="#fff" stroke-width="1.1">
        <circle cx="0" cy="-80" r="6"/><path d="M-2 -82h3a1.5 1.5 0 0 1 0 3h-2a1.5 1.5 0 0 0 0 3h3M0 -84v10"/>
        <path d="M62 -60v-6M66 -60v-9M70 -60v-12M58 -58h16"/>
        <circle cx="79" cy="-1" r="7"/><circle cx="79" cy="-1" r="3"/><path d="M79 -1l8 -8"/>
        <ellipse cx="75" cy="60" rx="6" ry="2"/><path d="M69 60v8M81 60v8"/><ellipse cx="75" cy="68" rx="6" ry="2"/>
        <circle cx="6" cy="82" r="3"/><circle cx="14" cy="82" r="3"/><circle cx="22" cy="82" r="3"/><path d="M2 91a4 4 0 0 1 8 0M10 91a4 4 0 0 1 8 0M18 91a4 4 0 0 1 8 0"/>
      </g>
    </g>
  </svg>

  <div class="title-blue abs" style="left:209px;top:64px;font-size:18.5px">MARKET OPPORTUNITIES</div>
  <div class="opp" style="top:90px">
    <div class="opp-item"><svg width="22" height="22" viewBox="0 0 22 22" fill="none" stroke="#3c4fc8" stroke-width="1.2"><path d="M7 5h8l-2 3a7 7 0 1 1-4 0z"/><text x="11" y="18" font-size="8" text-anchor="middle" fill="#3c4fc8" stroke="none">$</text></svg><div><h4>TITLE</h4><p>It is a process to allow an organization to focus resources on the greatest opportunities to increase sales and achieve the company's target.</p></div></div>
    <div class="opp-item"><svg width="22" height="22" viewBox="0 0 22 22" fill="none" stroke="#3c4fc8" stroke-width="1.2"><path d="M3 18v-6h4v6M9 18v-9h4v9M15 18v-13h4v13"/></svg><div><h4>TITLE</h4><p>Research your target group and narrow your market.</p></div></div>
    <div class="opp-item"><svg width="22" height="22" viewBox="0 0 22 22" fill="none" stroke="#3c4fc8" stroke-width="1.2"><circle cx="10" cy="12" r="8"/><circle cx="10" cy="12" r="4"/><path d="M10 12l9-9"/></svg><div><h4>TITLE</h4><p>Your brand identity is a way to tell your brand story and position yourself from your competitors visually.</p></div></div>
    <div class="opp-item"><svg width="22" height="22" viewBox="0 0 22 22" fill="none" stroke="#3c4fc8" stroke-width="1.2"><ellipse cx="14" cy="5" rx="6" ry="2"/><path d="M8 5v10M20 5v10"/><ellipse cx="14" cy="15" rx="6" ry="2"/><circle cx="7" cy="15" r="5"/></svg><div><h4>TITLE</h4><p>Marketing strategy's objective is to increase sales and gain a competitive advantage over other competitors.</p></div></div>
    <div class="opp-item"><svg width="22" height="22" viewBox="0 0 22 22" fill="none" stroke="#3c4fc8" stroke-width="1.2"><circle cx="5" cy="8" r="3"/><circle cx="11" cy="7" r="3"/><circle cx="17" cy="8" r="3"/><path d="M1 17a4 4 0 0 1 8 0M7 17a4 4 0 0 1 8 0M13 17a4 4 0 0 1 8 0"/></svg><div><h4>TITLE</h4><p>A new way of how we purchase goods at fingertips in modern era.</p></div></div>
  </div>
</section>

<!-- Slide 6: rings and steps -->
<section class="slide s6">
  <div class="header-band" style="width:329px"></div>
  <div class="brand" style="left:339px"><span class="brand-mark"></span><div class="brand-name">Corvath<small>Therapeutics</small></div></div>
  <div class="header-cap"></div>

  <svg class="abs" style="left:0;top:60px" width="200" height="200" aria-hidden="true">
    <defs><linearGradient id="g-arc" x1="0" y1="0" x2="0" y2="1"><stop offset="0" stop-color="#8a2a9c"/><stop offset=".5" stop-color="#3c4fc8"/><stop offset="1" stop-color="#12b6ec"/></linearGradient></defs>
    <g fill="none" stroke="#e2e2e6" stroke-width="3.5">
      <circle cx="98" cy="94" r="74"/><circle cx="98" cy="94" r="60"/><circle cx="98" cy="94" r="46"/><circle cx="98" cy="94" r="32"/>
    </g>
    <g fill="none" stroke-width="3.5">
      <circle cx="98" cy="94" r="74" stroke="url(#g-arc)" stroke-dasharray="280 500" transform="rotate(-90 98 94)"/>
      <circle cx="98" cy="94" r="60" stroke="#1b3fa0" stroke-dasharray="215 500" transform="rotate(-90 98 94)"/>
      <circle cx="98" cy="94" r="46" stroke="#3c4fc8" stroke-dasharray="150 500" transform="rotate(-90 98 94)"/>
      <circle cx="98" cy="94" r="32" stroke="#12b6ec" stroke-dasharray="75 500" transform="rotate(-90 98 94)"/>
    </g>
  </svg>

  <span class="num" style="left:190px;top:78px;background:#6b2a9c"></span>
  <span class="num" style="left:190px;top:117px;background:#9a2a9c"></span>
  <span class="num" style="left:190px;top:156px;background:linear-gradient(135deg,#12b6ec,#1b6fd0)"></span>
  <span class="num" style="left:190px;top:196px;background:linear-gradient(135deg,#3c86d6,#1b6fd0)"></span>
  <div class="num-text tiny" style="left:238px;top:75px"><b>01</b>Lorem ipsum dolor<br>sit amet consectetur<br>adipiscing elit, sed do</div>
  <div class="num-text tiny" style="left:238px;top:113px"><b>02</b>Lorem ipsum dolor<br>sit amet consectetur<br>adipiscing elit, sed do</div>
  <div class="num-text tiny" style="left:238px;top:154px"><b>03</b>Lorem ipsum dolor<br>sit amet consectetur<br>adipiscing elit, sed do</div>
  <div class="num-text tiny" style="left:238px;top:194px"><b>04</b>Lorem ipsum dolor<br>sit amet consectetur<br>adipiscing elit, sed do</div>

  <div class="title-blue abs" style="left:328px;top:79px;font-size:19px">TITLE HERE</div>
  <ul class="checklist" style="left:328px;top:110px;width:140px">
    <li style="margin-bottom:10px"><svg width="20" height="20" viewBox="0 0 18 18"><rect x="1" y="3" width="14" height="14" fill="none" stroke="#3c4fc8" stroke-width="1.6"/><path d="M4 10l4 4 9-12" fill="none" stroke="#3c4fc8" stroke-width="1.8"/></svg><span class="small" style="font-size:6.4px;line-height:7.4px">Lorem ipsum dolor sit amet, consectetur adipiscing elit. Etiam iaculis commodo.</span></li>
    <li style="margin-bottom:10px"><svg width="20" height="20" viewBox="0 0 18 18"><rect x="1" y="3" width="14" height="14" fill="none" stroke="#3c4fc8" stroke-width="1.6"/><path d="M4 10l4 4 9-12" fill="none" stroke="#3c4fc8" stroke-width="1.8"/></svg><span class="small" style="font-size:6.4px;line-height:7.4px">Lorem ipsum dolor sit amet, consectetur adipiscing elit. Etiam iaculis commod.</span></li>
    <li style="margin-bottom:10px"><svg width="20" height="20" viewBox="0 0 18 18"><rect x="1" y="3" width="14" height="14" fill="none" stroke="#3c4fc8" stroke-width="1.6"/><path d="M4 10l4 4 9-12" fill="none" stroke="#3c4fc8" stroke-width="1.8"/></svg><span class="small" style="font-size:6.4px;line-height:7.4px">Lorem ipsum dolor sit amet, consectetur adipiscing elit. Etiam iaculis commod.</span></li>
    <li><svg width="20" height="20" viewBox="0 0 18 18"><rect x="1" y="3" width="14" height="14" fill="none" stroke="#3c4fc8" stroke-width="1.6"/><path d="M4 10l4 4 9-12" fill="none" stroke="#3c4fc8" stroke-width="1.8"/></svg><span class="small" style="font-size:6.4px;line-height:7.4px">Lorem ipsum dolor sit amet, consectetur adipiscing elit. Etiam iaculis commod.</span></li>
  </ul>
</section>

</body>
</html>
```